Business Cards using attached files

Please make new business cards using files attached. I would like something a little more updated possibly. Double sided.
I am wanting to make sure I can change the names and positions easily myself.

Target Market(s)

Automotive Repair

Industry/Entity Type

Automotive

Contact Information for Business Card

See attached files

Font styles to use
Serif

Colors
0054AA
0677BA
7BADD7
CADEEF
E8F1F8

Requirements
Must have
• Red white blue colors
Nice to have
• I'd like it slightly updated from our existing design. Double sided. I'd like to be able to change names and positions easily to have them printed.
Should not have
• I'm not sure

```html
<!DOCTYPE html>
<html lang="en">
<head>
<meta charset="utf-8">
<title>Harbor Lane Auto &amp; Truck Center – Business Card</title>
<link rel="stylesheet" href="https://fonts.googleapis.com/css2?family=Libre+Baskerville:wght@400;700&family=Roboto+Condensed:wght@400;700&family=Arimo:wght@400;700&display=swap">
<style>
  :root {
    --navy: #1d3b63;
    --red: #c8272d;
    --ink: #2b2b2b;
    --grey-text: #4a4a4a;
    --card: #ffffff;
    --card-back: #f7f7f7;
    --page: #e6e7e9;
    --map-fill: #d9dadc;
  }
  * { margin: 0; padding: 0; box-sizing: border-box; }
  html, body { width: 1200px; height: 751px; overflow: hidden; }
  body { background: var(--page); position: relative; font-family: "Arimo", Arial, sans-serif; color: var(--ink); }

  .card { position: absolute; left: 353px; width: 494px; height: 283px; border-radius: 14px; overflow: hidden; }
  .card--front { top: 82px; background: var(--card); }
  .card--back { top: 394px; background: var(--card-back); }

  /* Front */
  .brand { position: absolute; right: 34px; top: 66px; display: flex; align-items: center; gap: 8px;
    font-family: "Libre Baskerville", Georgia, serif; font-weight: 700; font-size: 24px; color: var(--navy); }
  .brand__dot { width: 14px; height: 14px; border-radius: 50%; background: var(--red); }

  .person { position: absolute; left: 34px; top: 144px; }
  .person__name { font-family: "Libre Baskerville", Georgia, serif; font-size: 19px; color: var(--red); line-height: 1; }
  .person__role { font-size: 11px; font-weight: 700; color: var(--navy); margin-top: 4px; }

  .rule { position: absolute; left: 34px; right: 30px; top: 177px; height: 1.5px; background: var(--navy); }

  .address { position: absolute; right: 30px; top: 160px; font-size: 12.5px; display: flex; align-items: center; gap: 4px; }
  .contact { position: absolute; font-size: 12.5px; line-height: 15px; }
  .contact--left { left: 34px; top: 183px; }
  .contact--right { right: 30px; top: 183px; text-align: right; }
  .contact__row { display: flex; align-items: center; gap: 6px; }
  .contact--right .contact__row { justify-content: flex-end; }
  .icon { width: 11px; height: 11px; flex: none; fill: var(--navy); }

  .swoosh { position: absolute; left: 0; bottom: 0; width: 494px; height: 70px; }

  /* Back */
  .promise { position: absolute; left: 30px; top: 28px; font-family: "Roboto Condensed", "Arial Narrow", sans-serif; }
  .promise__title { font-size: 17px; font-weight: 700; color: var(--red); }
  .promise__list { list-style: none; margin-top: 12px; }
  .promise__item { display: flex; align-items: center; gap: 8px; font-size: 12px; color: var(--grey-text); height: 18px; }
  .tick { width: 11px; height: 11px; flex: none; }

  .online { position: absolute; left: 32px; top: 214px; }
  .online__title { font-size: 12.5px; font-weight: 700; color: var(--red); }
  .online__url { font-size: 12.5px; color: var(--grey-text); }
  .social { display: flex; gap: 3px; margin-top: 7px; }
  .social__dot { width: 15px; height: 15px; border-radius: 50%; background: var(--red); }

  .map { position: absolute; left: 274px; top: 20px; width: 195px; height: 190px; border: 3px solid #111; background: var(--map-fill); }
  .location { position: absolute; left: 264px; width: 215px; top: 226px; text-align: center; font-size: 12px; color: var(--grey-text); line-height: 14px; }
  .location__name { font-family: "Libre Baskerville", Georgia, serif; font-weight: 700; font-size: 11.5px; color: #111; margin-bottom: 2px; }
</style>
</head>
<body>

<section class="card card--front" aria-label="Business card front">
  <div class="brand"><span class="brand__dot"></span>Harbor Lane</div>

  <div class="person">
    <div class="person__name">Dana Whitlock</div>
    <div class="person__role">Service Advisor</div>
  </div>

  <div class="address">418 Route 72 Millbrook, NY 11890
    <svg class="icon" viewBox="0 0 12 12"><path d="M6 0.5a4 4 0 0 0-4 4c0 3 4 7 4 7s4-4 4-7a4 4 0 0 0-4-4zm0 5.6a1.6 1.6 0 1 1 0-3.2 1.6 1.6 0 0 1 0 3.2z"/></svg>
  </div>
  <div class="rule"></div>

  <div class="contact contact--left">
    <div class="contact__row">
      <svg class="icon" viewBox="0 0 12 12"><path d="M2.5 0.8l2 2.3-1.1 1.5c.7 1.5 1.9 2.7 3.3 3.4l1.5-1.1 2.3 2-1.1 1.9C5.5 10.8 1.2 6.5 0.6 2z"/></svg>
      (555) 210-4471
    </div>
    <div class="contact__row">
      <svg class="icon" viewBox="0 0 12 12"><rect x="3" y="0.5" width="6" height="3"/><rect x="0.5" y="4" width="11" height="5" rx="1"/><rect x="3" y="8" width="6" height="3.5" fill="#fff" stroke="#1d3b63"/></svg>
      (555) 210-4478
    </div>
  </div>

  <div class="contact contact--right">
    <div class="contact__row">dana@harborlaneauto.com
      <svg class="icon" viewBox="0 0 12 12"><rect x="0.5" y="2" width="11" height="8"/><path d="M0.5 2l5.5 4.5 5.5-4.5" fill="none" stroke="#fff"/></svg>
    </div>
    <div class="contact__row">www.harborlaneauto.com
      <svg class="icon" viewBox="0 0 12 12"><circle cx="6" cy="6" r="5.5"/><path d="M0.5 6h11M6 0.5c-2.5 3-2.5 8 0 11M6 0.5c2.5 3 2.5 8 0 11" fill="none" stroke="#fff" stroke-width=".8"/></svg>
    </div>
  </div>

  <svg class="swoosh" viewBox="0 0 494 70" preserveAspectRatio="none" aria-hidden="true">
    <path d="M0 10 C140 20 330 40 494 20 L494 70 L0 70 Z" fill="var(--red)"/>
    <path d="M0 6 C140 18 330 38 494 18 L494 22 C330 42 140 28 0 18 Z" fill="#fff"/>
    <path d="M0 0 C150 10 300 30 494 14 L494 17 C320 36 150 24 0 13 Z" fill="var(--navy)"/>
  </svg>
</section>

<section class="card card--back" aria-label="Business card back">
  <div class="promise">
    <h2 class="promise__title">We Stand Behind Our Service</h2>
    <ul class="promise__list">
      <li class="promise__item"><svg class="tick" viewBox="0 0 12 12"><circle cx="6" cy="6" r="6" fill="#1d3b63"/><path d="M3.3 6.2l1.8 1.8 3.6-3.8" fill="none" stroke="#fff" stroke-width="1.5"/></svg>Family Owned &amp; Operated</li>
      <li class="promise__item"><svg class="tick" viewBox="0 0 12 12"><circle cx="6" cy="6" r="6" fill="#1d3b63"/><path d="M3.3 6.2l1.8 1.8 3.6-3.8" fill="none" stroke="#fff" stroke-width="1.5"/></svg>Complimentary 2 year / 24,000 mile Warranty</li>
      <li class="promise__item"><svg class="tick" viewBox="0 0 12 12"><circle cx="6" cy="6" r="6" fill="#1d3b63"/><path d="M3.3 6.2l1.8 1.8 3.6-3.8" fill="none" stroke="#fff" stroke-width="1.5"/></svg>Free local Pickup/dropoff service</li>
      <li class="promise__item"><svg class="tick" viewBox="0 0 12 12"><circle cx="6" cy="6" r="6" fill="#1d3b63"/><path d="M3.3 6.2l1.8 1.8 3.6-3.8" fill="none" stroke="#fff" stroke-width="1.5"/></svg>Experts In Domestic &amp; Import Service</li>
      <li class="promise__item"><svg class="tick" viewBox="0 0 12 12"><circle cx="6" cy="6" r="6" fill="#1d3b63"/><path d="M3.3 6.2l1.8 1.8 3.6-3.8" fill="none" stroke="#fff" stroke-width="1.5"/></svg>Factory Certified Mechanics</li>
      <li class="promise__item"><svg class="tick" viewBox="0 0 12 12"><circle cx="6" cy="6" r="6" fill="#1d3b63"/><path d="M3.3 6.2l1.8 1.8 3.6-3.8" fill="none" stroke="#fff" stroke-width="1.5"/></svg>Diesel &amp; Fleet Services Available</li>
      <li class="promise__item"><svg class="tick" viewBox="0 0 12 12"><circle cx="6" cy="6" r="6" fill="#1d3b63"/><path d="M3.3 6.2l1.8 1.8 3.6-3.8" fill="none" stroke="#fff" stroke-width="1.5"/></svg>Honest, Knowledgeable, Trustworthy Service</li>
      <li class="promise__item"><svg class="tick" viewBox="0 0 12 12"><circle cx="6" cy="6" r="6" fill="#1d3b63"/><path d="M3.3 6.2l1.8 1.8 3.6-3.8" fill="none" stroke="#fff" stroke-width="1.5"/></svg>Top Rated A+ Auto Repair Facility</li>
    </ul>
  </div>

  <div class="online">
    <div class="online__title">Find Us Online</div>
    <div class="online__url">www.harborlaneauto.com</div>
    <div class="social"><span class="social__dot"></span><span class="social__dot"></span><span class="social__dot"></span></div>
  </div>

  <div class="map" role="img" aria-label="Street map showing the shop location near the main route and parkway"></div>

  <div class="location">
    <div class="location__name">Harbor Lane Auto &amp; Truck Center</div>
    418 Route 72<br>Millbrook, NY 11890
  </div>
</section>

</body>
</html>
```